FungaVita Nutrition Require Label Design Assistance

We are FungaVita!

We are a new mushroom focused nutrition supplement company looking for some design assistance. We are looking to provide some of the highest quality mushroom supplements available on the market today, using 100% fruiting bodies where many other companies opt for cheaper alternatives. We strongly believe in the power of mushroom nutrition and wish to focus on the high-end supplement market.

We are starting with three initial ranges; Lions Mane, Turkey Tail and Reishi - and wish to have powerful yet elegant designs for each. We wish to be visually appealing whilst maintaining the high-end feel. Imagery of the mushrooms on the label would be good if it maintains high-end appeal. Our bottles will be dark green and lids will be white if this helps with visualization. We have a logo and preferred font for the name which can be used if possible. The image in the logo may need resizing to fit with the supplement market (smaller logo/larger font). If you provide a superior logo to that which we currently have, we would consider using it.

The three range designs should be the same, but with the mushroom name and any imagery changed to reflect the different ranges. I am happy to supply images where required.

Label dimensions = 55mm x 150mm

Target Market(s)

Premium High End Health Supplements

Industry/Entity Type

Supplement

Font styles to use
Serif
Sans Serif

Colors

Designer to choose colors to be used in the design.

Requirements
Must have
• Must have the text "100% Fruiting Bodies"
• Must have Organic + Vegan notification.
• Must have an ingredients section, and there will need to be some space for small-print (which will be decided on shortly).
Nice to have
• See label specifications in message thread.

```html
<!DOCTYPE html>
<html lang="en">
<head>
<meta charset="utf-8">
<title>FungaVita Label Range</title>
<link href="https://fonts.googleapis.com/css2?family=Playfair+Display:wght@700;800&family=Roboto:wght@300;400&display=swap" rel="stylesheet">
<style>
  :root{
    --slate:#48595a;
    --lime:#a6ff00;
    --lemon:#f8f53a;
    --gold:#b08a3e;
    --white:#ffffff;
    --mist:#f6f6f6;
    --ink:#1a1a1a;
  }
  *{box-sizing:border-box;margin:0;padding:0}
  html,body{width:1200px;height:885px;overflow:hidden;background:var(--slate)}
  .canvas{position:relative;width:1200px;height:885px;background:var(--slate)}
  .label{position:absolute;width:525px;height:403px;background:var(--white);overflow:hidden;font-family:"Roboto",Arial,sans-serif}
  .label--turkey{left:49px;top:35px}
  .label--lions{left:627px;top:35px}
  .label--reishi{left:311px;top:463px}

  .band-left{position:absolute;left:0;top:0;width:84px;height:100%;background:var(--lime)}
  .stripe{position:absolute;left:405px;top:0;width:11px;height:100%;background:var(--lemon)}
  .band-right{position:absolute;left:416px;top:0;width:109px;height:100%;background:var(--lime)}

  .ingredients{position:absolute;right:calc(525px - 73px);top:48px;writing-mode:vertical-rl;color:var(--white);font-weight:300;font-size:13.5px;line-height:15.5px}
  .ingredient{display:flex;justify-content:space-between;inline-size:260px}

  .brand{position:absolute;left:84px;width:321px;text-align:center;color:var(--gold)}
  .brand__ring{position:absolute;left:50%;top:52px;width:40px;height:40px;margin-left:-20px;border:2px solid var(--gold);border-radius:50%}
  .brand__name{position:absolute;left:0;right:0;top:106px;font-size:12px;font-weight:400;letter-spacing:2.5px;text-transform:uppercase}

  .cap{position:absolute;left:0;top:0}
  .arc{position:absolute;left:0;top:0;font-family:"Roboto",Arial,sans-serif;font-size:15px;font-weight:400;fill:var(--ink)}

  .product{position:absolute;left:84px;width:325px;text-align:center}
  .product__title{position:absolute;left:0;right:0;top:213px;font-family:"Playfair Display",Georgia,serif;font-weight:800;font-size:37px;line-height:30px;color:var(--gold);transform:scaleX(.78);letter-spacing:.5px}
  .product__claim{position:absolute;left:0;right:0;top:279px;font-size:19px;font-weight:400;line-height:16px;color:var(--ink)}
  .product__plus{display:block;font-size:14px;line-height:10px}
  .product__count{position:absolute;left:0;right:0;top:323px;font-size:25px;font-weight:300;line-height:22px;color:var(--gold)}
  .product__unit{position:absolute;left:0;right:0;top:344px;font-size:6.5px;color:var(--ink)}

  .side{position:absolute;left:416px;width:109px;text-align:center;color:var(--white)}
  .side__claim{position:absolute;left:0;right:0;top:298px;font-size:11.5px;font-weight:300}
  .side__ring{position:absolute;left:50%;top:327px;width:30px;height:30px;margin-left:-15px;border:2px solid var(--white);border-radius:50%}
  .side__name{position:absolute;left:0;right:0;top:367px;font-size:9px;letter-spacing:2px;text-transform:uppercase}
</style>
</head>
<body>
<div class="canvas">

  <!-- Turkey Tail -->
  <section class="label label--turkey">
    <div class="band-left"></div>
    <div class="stripe"></div>
    <div class="band-right"></div>
    <div class="ingredients">
      <div class="ingredient"><span>Turkey Tail Organic Fruiting Bodies</span><span>600mg</span></div>
      <div class="ingredient"><span>Organic Enoki Extract</span><span>25mg</span></div>
      <div class="ingredient"><span>Curcumin</span><span>100mg</span></div>
    </div>
    <div class="brand"><div class="brand__ring"></div><div class="brand__name">FungaVita</div></div>
    <svg class="cap" width="525" height="403" viewBox="0 0 525 403" role="img" aria-label="Photograph of turkey tail mushrooms growing on mossy wood">
      <defs>
        <linearGradient id="turkeyFill" x1="0" y1="0" x2="1" y2="0">
          <stop offset="0" stop-color="#6b7a22"/>
          <stop offset=".45" stop-color="#d9a46a"/>
          <stop offset=".75" stop-color="#c88a55"/>
          <stop offset="1" stop-color="#4a3f1e"/>
        </linearGradient>
      </defs>
      <path fill="var(--mist)" d="M104,222 C112,150 180,98 250,98 C322,98 384,140 392,208 C394,226 382,230 368,227 C330,216 290,208 248,208 C205,208 165,216 126,228 C110,232 102,232 104,222 Z"/>
      <path fill="url(#turkeyFill)" d="M118,214 C130,150 190,110 250,110 C315,110 372,150 380,205 C382,215 376,218 368,216 C330,205 290,196 248,196 C205,196 165,205 128,216 C120,218 116,218 118,214 Z"/>
    </svg>
    <svg class="arc" width="525" height="403" viewBox="0 0 525 403">
      <path id="arcTurkey" fill="none" d="M270,100 C322,106 372,142 392,202"/>
      <text><textPath href="#arcTurkey">% 100 Fruiting Bodies</textPath></text>
    </svg>
    <div class="product">
      <div class="product__title">TURKEY<br>TAIL</div>
      <div class="product__claim">Organic<span class="product__plus">+</span>Vegan</div>
      <div class="product__count">60</div>
      <div class="product__unit">capsules</div>
    </div>
    <div class="side"><div class="side__claim">Organic+Vegan</div><div class="side__ring"></div><div class="side__name">FungaVita</div></div>
  </section>

  <!-- Lions Mane -->
  <section class="label label--lions">
    <div class="band-left"></div>
    <div class="stripe"></div>
    <div class="band-right"></div>
    <div class="ingredients">
      <div class="ingredient"><span>Lions Mane Organic Fruiting Bodies</span><span>700mg</span></div>
      <div class="ingredient"><span>Ginko Bilbao</span><span>35mg</span></div>
    </div>
    <div class="brand"><div class="brand__ring"></div><div class="brand__name">FungaVita</div></div>
    <svg class="cap" width="525" height="403" viewBox="0 0 525 403" role="img" aria-label="Photograph of a white lion's mane mushroom against dark forest">
      <defs>
        <linearGradient id="lionsFill" x1="0" y1="0" x2="1" y2="0">
          <stop offset="0" stop-color="#2f3a33"/>
          <stop offset=".25" stop-color="#c9d0cf"/>
          <stop offset=".6" stop-color="#e6ebea"/>
          <stop offset=".85" stop-color="#9ca9a4"/>
          <stop offset="1" stop-color="#2e4a2c"/>
        </linearGradient>
      </defs>
      <path fill="var(--mist)" d="M104,222 C112,150 180,98 250,98 C322,98 384,140 392,208 C394,226 382,230 368,227 C330,216 290,208 248,208 C205,208 165,216 126,228 C110,232 102,232 104,222 Z"/>
      <path fill="url(#lionsFill)" d="M118,214 C130,150 190,110 250,110 C315,110 372,150 380,205 C382,215 376,218 368,216 C330,205 290,196 248,196 C205,196 165,205 128,216 C120,218 116,218 118,214 Z"/>
    </svg>
    <svg class="arc" width="525" height="403" viewBox="0 0 525 403">
      <path id="arcLions" fill="none" d="M270,102 C322,108 372,144 392,204"/>
      <text><textPath href="#arcLions">% 100 Fruiting Bodies</textPath></text>
    </svg>
    <div class="product">
      <div class="product__title">LIONS<br>MANE</div>
      <div class="product__claim">Organic<span class="product__plus">+</span>Vegan</div>
      <div class="product__count">60</div>
      <div class="product__unit">capsules</div>
    </div>
    <div class="side"><div class="side__claim">Organic+Vegan</div><div class="side__ring"></div><div class="side__name">FungaVita</div></div>
  </section>

  <!-- Reishi -->
  <section class="label label--reishi">
    <div class="band-left"></div>
    <div class="stripe"></div>
    <div class="band-right"></div>
    <div class="ingredients">
      <div class="ingredient"><span>Reishi Organic Fruiting Bodies</span><span>700mg</span></div>
      <div class="ingredient"><span>Green Tea Powder</span><span>35mg</span></div>
    </div>
    <div class="brand"><div class="brand__ring"></div><div class="brand__name">FungaVita</div></div>
    <svg class="cap" width="525" height="403" viewBox="0 0 525 403" role="img" aria-label="Photograph of layered red-brown reishi mushrooms">
      <defs>
        <linearGradient id="reishiFill" x1="0" y1="0" x2="1" y2="0">
          <stop offset="0" stop-color="#8a5a3a"/>
          <stop offset=".35" stop-color="#a5493b"/>
          <stop offset=".7" stop-color="#7a2e24"/>
          <stop offset="1" stop-color="#3f1c16"/>
        </linearGradient>
      </defs>
      <path fill="var(--mist)" d="M104,222 C112,150 180,98 250,98 C322,98 384,140 392,208 C394,226 382,230 368,227 C330,216 290,208 248,208 C205,208 165,216 126,228 C110,232 102,232 104,222 Z"/>
      <path fill="url(#reishiFill)" d="M118,214 C130,150 190,110 250,110 C315,110 372,150 380,205 C382,215 376,218 368,216 C330,205 290,196 248,196 C205,196 165,205 128,216 C120,218 116,218 118,214 Z"/>
    </svg>
    <svg class="arc" width="525" height="403" viewBox="0 0 525 403">
      <path id="arcReishi" fill="none" d="M270,100 C322,106 372,142 392,202"/>
      <text><textPath href="#arcReishi">% 100 Fruiting Bodies</textPath></text>
    </svg>
    <div class="product">
      <div class="product__title" style="top:244px">REISHI</div>
      <div class="product__claim">Organic<span class="product__plus">+</span>Vegan</div>
      <div class="product__count">60</div>
      <div class="product__unit">capsules</div>
    </div>
    <div class="side"><div class="side__claim">Organic+Vegan</div><div class="side__ring"></div><div class="side__name">FungaVita</div></div>
  </section>

</div>
</body>
</html>
```